VELANTRA
Mobile Ultrasound
Simple
Danielle Morvek RDMS RDCS RVT
President
P.O. Box 48617 Las Vegas, NV 89120-4861
info@velantramobilescan.example
www.velantramobilescan.example

```html
<!DOCTYPE html>
<html lang="en">
<head>
<meta charset="utf-8">
<title>Velantra Mobile Ultrasound – Stationery</title>
<link href="https://fonts.googleapis.com/css2?family=Open+Sans:wght@400;600;700;800&display=swap" rel="stylesheet">
<style>
  :root {
    --stage: #ececec;
    --paper: #ffffff;
    --brand-blue: #1b6fae;
    --brand-blue-light: #3d94d1;
    --brand-grey: #8d9196;
    --brand-grey-light: #c9ccd0;
    --ink: #3b3f44;
    --ink-soft: #6c7177;
    --faint: #e4edf4;
  }
  * { box-sizing: border-box; margin: 0; padding: 0; }
  html, body { width: 1200px; height: 497px; overflow: hidden; }
  body {
    position: relative;
    background: var(--stage);
    font-family: "Open Sans", Arial, sans-serif;
    color: var(--ink);
  }
  .sheet {
    position: absolute;
    background: var(--paper);
    overflow: hidden;
    box-shadow: 0 2px 6px rgba(0,0,0,.18);
  }
  .sheet svg.swoosh { position: absolute; inset: 0; width: 100%; height: 100%; }

  .brand { position: absolute; display: flex; align-items: center; gap: 6px; }
  .brand-dot { border-radius: 50%; background: var(--brand-grey); flex: none; }
  .brand-text { display: flex; flex-direction: column; line-height: 1; }
  .brand-name { font-weight: 800; color: var(--brand-blue); letter-spacing: .04em; }
  .brand-tag { font-weight: 600; color: var(--brand-grey); letter-spacing: .22em; text-transform: uppercase; margin-top: 2px; }

  .faint-circle { position: absolute; border-radius: 50%; background: var(--faint); }

  .contact { position: absolute; font-size: 5px; line-height: 1.45; color: var(--ink-soft); }
  .contact .person { font-weight: 700; color: var(--brand-blue); font-size: 6px; }

  /* business cards */
  .card { top: 65px; width: 197px; height: 139px; }
  .card--front { left: 22px; }
  .card--back { left: 228px; }
  .card .brand { left: 12px; top: 12px; }
  .card .brand-dot { width: 22px; height: 22px; }
  .card .brand-name { font-size: 15px; }
  .card .brand-tag { font-size: 4.5px; }
  .card .contact { left: 14px; top: 62px; }

  /* letterhead */
  .letterhead { left: 432px; top: 29px; width: 302px; height: 410px; }
  .letterhead .brand { left: 18px; top: 18px; }
  .letterhead .brand-dot { width: 28px; height: 28px; }
  .letterhead .brand-name { font-size: 19px; }
  .letterhead .brand-tag { font-size: 5.5px; }
  .letterhead .contact { left: 188px; top: 22px; }
  .letterhead .faint-circle { left: 40px; top: 170px; width: 70px; height: 70px; }

  /* envelopes */
  .envelope-back { left: 770px; top: 28px; width: 340px; height: 150px; }
  .envelope-middle { left: 792px; top: 106px; width: 318px; height: 150px; }
  .envelope-front { left: 736px; top: 230px; width: 372px; height: 205px; }
  .envelope-back .brand-dot { position: absolute; left: 148px; top: 12px; width: 44px; height: 44px; background: var(--ink); }
  .envelope-front .brand { left: 18px; top: 36px; }
  .envelope-front .brand-dot { width: 28px; height: 28px; }
  .envelope-front .brand-name { font-size: 19px; }
  .envelope-front .brand-tag { font-size: 5.5px; }
  .envelope-front .contact { left: 22px; top: 138px; }
  .envelope-front .faint-circle { right: 26px; top: 62px; width: 90px; height: 90px; }
</style>
</head>
<body>

  <!-- business card, front -->
  <section class="sheet card card--front">
    <svg class="swoosh" viewBox="0 0 197 139" preserveAspectRatio="none" aria-hidden="true">
      <path d="M120 0 Q165 20 197 10 L197 0 Z" fill="var(--brand-grey-light)"/>
      <path d="M0 139 Q90 110 197 125 L197 139 Z" fill="var(--brand-grey-light)"/>
      <path d="M150 139 Q175 100 197 90 L197 139 Z" fill="var(--brand-blue)"/>
    </svg>
    <div class="brand">
      <span class="brand-dot"></span>
      <span class="brand-text"><span class="brand-name">VELANTRA</span><span class="brand-tag">Mobile Ultrasound</span></span>
    </div>
    <div class="contact">
      <div class="person">Danielle Morvek</div>
      <div>RDMS RDCS RVT</div>
      <div>President</div>
      <div>P.O. Box 48617 Las Vegas, NV 89120-4861</div>
      <div>Tel 702.555.0148 · Fax 702.555.0149</div>
      <div>info@velantramobilescan.example</div>
      <div>www.velantramobilescan.example</div>
    </div>
  </section>

  <!-- business card, second version -->
  <section class="sheet card card--back">
    <svg class="swoosh" viewBox="0 0 197 139" preserveAspectRatio="none" aria-hidden="true">
      <path d="M130 0 Q170 30 197 40 L197 0 Z" fill="var(--brand-grey)"/>
      <path d="M0 139 Q100 112 197 122 L197 139 Z" fill="var(--brand-blue)"/>
    </svg>
    <div class="brand">
      <span class="brand-dot"></span>
      <span class="brand-text"><span class="brand-name">VELANTRA</span><span class="brand-tag">Mobile Ultrasound</span></span>
    </div>
    <div class="contact">
      <div class="person">Danielle Morvek</div>
      <div>RDMS RDCS RVT</div>
      <div>President</div>
      <div>P.O. Box 48617 Las Vegas, NV 89120-4861</div>
      <div>Tel 702.555.0148 · Fax 702.555.0149</div>
      <div>info@velantramobilescan.example</div>
      <div>www.velantramobilescan.example</div>
    </div>
  </section>

  <!-- letterhead -->
  <section class="sheet letterhead">
    <svg class="swoosh" viewBox="0 0 302 410" preserveAspectRatio="none" aria-hidden="true">
      <path d="M0 0 L80 0 Q30 30 0 60 Z" fill="var(--brand-blue)"/>
      <path d="M0 410 Q150 385 302 395 L302 410 Z" fill="var(--brand-grey-light)"/>
      <path d="M250 410 Q280 370 302 360 L302 410 Z" fill="var(--brand-blue)"/>
    </svg>
    <div class="brand">
      <span class="brand-dot"></span>
      <span class="brand-text"><span class="brand-name">VELANTRA</span><span class="brand-tag">Mobile Ultrasound</span></span>
    </div>
    <div class="contact">
      <div>P.O. Box 48617</div>
      <div>Las Vegas, NV 89120-4861</div>
      <div>Tel 702.555.0148</div>
      <div>info@velantramobilescan.example</div>
    </div>
    <span class="faint-circle"></span>
  </section>

  <!-- envelope, flap side -->
  <section class="sheet envelope-back">
    <svg class="swoosh" viewBox="0 0 340 150" preserveAspectRatio="none" aria-hidden="true">
      <path d="M0 0 L170 70 L340 0 Z" fill="var(--brand-grey-light)"/>
      <path d="M0 0 L170 70 L340 0" fill="none" stroke="var(--brand-grey)" stroke-width="1"/>
    </svg>
    <span class="brand-dot"></span>
  </section>

  <!-- envelope, open flap -->
  <section class="sheet envelope-middle">
    <svg class="swoosh" viewBox="0 0 318 150" preserveAspectRatio="none" aria-hidden="true">
      <path d="M0 20 L159 80 L318 20" fill="none" stroke="var(--brand-grey-light)" stroke-width="1.2"/>
      <path d="M0 150 L140 85 M318 150 L178 85" fill="none" stroke="var(--brand-grey-light)" stroke-width="1"/>
    </svg>
  </section>

  <!-- envelope, address side -->
  <section class="sheet envelope-front">
    <svg class="swoosh" viewBox="0 0 372 205" preserveAspectRatio="none" aria-hidden="true">
      <path d="M0 0 L372 0 L372 35 Q200 5 90 30 Q40 40 0 70 Z" fill="var(--brand-blue)"/>
      <path d="M90 30 Q200 5 372 35 L372 42 Q210 15 100 36 Z" fill="var(--brand-blue-light)"/>
    </svg>
    <div class="brand">
      <span class="brand-dot"></span>
      <span class="brand-text"><span class="brand-name">VELANTRA</span><span class="brand-tag">Mobile Ultrasound</span></span>
    </div>
    <div class="contact">
      <div>P.O. Box 48617</div>
      <div>Las Vegas, NV 89120-4861</div>
      <div>Tel 702.555.0148</div>
      <div>www.velantramobilescan.example</div>
    </div>
    <span class="faint-circle"></span>
  </section>

</body>
</html>
```